Awesome Business Card Design needed!

Hey there.
I'm looking for a simple but awesome business card design.
Type of company: Online advertisement agency
(please don't use the typical business people or statistics images on the card)
The front has to display the business name
and possibly some sort of logo ( perhaps something with the two M's of the biz name )
And the back of the card should say:
Name
Phone
Email
Let your imagination flow.
here are some designs that I like and that you can use as inspiration.
Simple but Awesome
http://images.pixelvane.example/designs/55128_877673_43091_thumbnail.jpg
http://images.pixelvane.example/designs/37714_747642_40106_image.jpg
http://images.pixelvane.example/designs/55128_877673_43091_image.jpg
http://images.pixelvane.example/designs/51321_781878_43091_image.jpg
http://images.pixelvane.example/designs/33378_399063_15912_image.jpg
http://images.pixelvane.example/designs/2337_271604_9495_image.jpg
good luck

```html
<!DOCTYPE html>
<html lang="en">
<head>
<meta charset="utf-8">
<title>Corvane Media – Business Card</title>
<link rel="stylesheet" href="https://fonts.googleapis.com/css2?family=Michroma&display=swap">
<style>
  :root {
    --backdrop: #5a5a5a;
    --card-top: #3a4040;
    --card-mid: #1f2424;
    --card-edge: #0b0d0d;
    --brand-blue: #5cbce6;
    --text-grey: #b9bcbc;
    --rule-grey: #6c7070;
  }
  html, body {
    margin: 0;
    width: 1200px;
    height: 534px;
    overflow: hidden;
    background: var(--backdrop);
    font-family: "Michroma", "Arial", sans-serif;
  }
  .canvas {
    position: relative;
    width: 1200px;
    height: 534px;
  }
  .card {
    position: absolute;
    top: 119px;
    width: 516px;
    height: 294px;
    overflow: hidden;
    background:
      radial-gradient(ellipse 70% 60% at 50% 30%, var(--card-top) 0%, var(--card-mid) 60%, var(--card-edge) 100%);
    box-shadow: 0 6px 18px rgba(0,0,0,0.45);
  }
  .card--front { left: 62px; }
  .card--back  { left: 620px; }

  .front-mark {
    position: absolute;
    left: 198px;
    top: 74px;
    width: 120px;
    height: 108px;
    background: var(--brand-blue);
  }
  .front-name {
    position: absolute;
    left: 0;
    right: 0;
    top: 196px;
    text-align: center;
    font-size: 20px;
    line-height: 24px;
    letter-spacing: 0.5px;
    color: var(--brand-blue);
  }

  .back-mark {
    position: absolute;
    left: 146px;
    top: 102px;
    width: 83px;
    height: 91px;
    background: var(--brand-blue);
  }
  .vertical {
    position: absolute;
    top: 0;
    height: 294px;
    writing-mode: vertical-rl;
    transform: rotate(180deg);
    white-space: nowrap;
    text-align: center;
  }
  .back-name {
    left: 244px;
    font-size: 16px;
    line-height: 16px;
    color: var(--brand-blue);
  }
  .person-name {
    left: 308px;
    font-size: 14px;
    line-height: 14px;
    letter-spacing: 1px;
    color: var(--text-grey);
  }
  .name-rule {
    position: absolute;
    left: 328px;
    top: 48px;
    width: 1px;
    height: 198px;
    background: var(--rule-grey);
  }
  .contact-phone {
    left: 342px;
    font-size: 9px;
    line-height: 9px;
    color: var(--text-grey);
  }
  .contact-email {
    left: 364px;
    font-size: 9px;
    line-height: 9px;
    color: var(--text-grey);
  }
</style>
</head>
<body>
<main class="canvas">
  <section class="card card--front" aria-label="Card front">
    <div class="front-mark"></div>
    <div class="front-name">CORVANE MEDIA</div>
  </section>

  <section class="card card--back" aria-label="Card back">
    <div class="back-mark"></div>
    <div class="vertical back-name">CORVANE MEDIA</div>
    <div class="vertical person-name">DANIEL HARPER</div>
    <div class="name-rule"></div>
    <div class="vertical contact-phone">P: 1555 014 2290</div>
    <div class="vertical contact-email">E: INFO@CORVANE.EXAMPLE</div>
  </section>
</main>
</body>
</html>
```